Each Small Lantern Non-profit brochure for fundraising

We are a small non-profit that works with at-risk children and orphans in our community (Salinas, CA) and around the world (Haiti). We work to meet the needs of the whole child...physical, emotional, social, and spiritual. We would like a simple, but inspiring and eye-catching brochure to give to businesses and individuals who are interested in partnering with us. We would like it to be two-sided, approximately 3" x 8" (fit in a business envelope).We would like it to include our logo, a quote or two from our supporters, and some pictures. Maybe some map graphics would be neat, too?

Our mission:
So this is who we are: a bunch of people who love Jesus and love and serve vulnerable kids at home and around the world. We want to meet the needs of the whole child as much as possible, by connecting them with the people in our community and lending our resources and gifts to do big things, a little at a time.

Quotes:
(If room)
"It fills up our hearts...to know that we can make a difference in one child's life, simply by giving school supplies. We hope beautiful Rosette feels loved." ~Dana Pollick and family, Salinas, CA

"For the same amount of money I easily spend on myself daily, I was helping this child have an education, shelter, food, a chance at life! He was so grateful, I was so grateful. I thought I would be making a difference in his life, but he made a huge difference in mine." ~Terry Vosbeck, Las Vegas, NV

Target Market(s)

corporate sponsors

Industry/Entity Type

Non Profit

Font styles to use
Sans Serif

Requirements
Must have
• Our mission statement and some pictures
• Mission:
• So this is who we are: a bunch of people who love Jesus and love and serve vulnerable kids at home and around the world. We want to meet the needs of the whole child as much as possible, by connecting them with the people in our community and lending our resources and gifts to do big things, a little at a time.
Nice to have
• Maybe a map as a background?
• Optional quotes to add: (Not necessary)
• "It fills up our hearts...to know that we can make a difference in one child's life, simply by giving school supplies. We hope beautiful Rosette feels loved." ~Dana Pollick and family, Salinas, CA
• "For the same amount of money I easily spend on myself daily, I was helping this child have an education, shelter, food, a chance at life! He was so grateful, I was so grateful. I thought I would be making a difference in his life, but he made a huge difference in mine." ~Terry Vosbeck, Las Vegas, NV
Should not have
• Sad looking children

```html
<!DOCTYPE html>
<html lang="en">
<head>
<meta charset="utf-8">
<title>Each Small Lantern – Who we are</title>
<link rel="stylesheet" href="https://fonts.googleapis.com/css2?family=Arimo:wght@400;700&display=swap">
<style>
  :root {
    --red: #e8141b;
    --white: #ffffff;
    --ink: #111111;
    --yellow: #fff200;
    --frame: #3a3a3a;
    --photo-warm: #8a7a5c;
    --photo-cool: #6f8fa0;
  }
  html, body {
    margin: 0;
    padding: 0;
    width: 1200px;
    height: 3200px;
    overflow: hidden;
    background: var(--white);
  }
  .panel {
    position: relative;
    width: 1200px;
    height: 3200px;
    overflow: hidden;
    background: var(--white);
    font-family: "Arimo", Arial, sans-serif;
    color: var(--ink);
  }
  .top-band {
    position: absolute;
    left: 0; top: 0;
    width: 1200px; height: 32px;
    background: var(--red);
  }
  .hero-photo {
    position: absolute;
    left: 0; top: 32px;
    width: 1168px; height: 790px;
    background: linear-gradient(160deg, #b9c4a4 0%, var(--photo-warm) 45%, #5b4a3a 100%);
  }
  .mission-shape {
    position: absolute;
    left: 0; top: 0;
    width: 1200px; height: 3200px;
  }
  .section-label {
    position: absolute;
    left: 72px; top: 820px;
    width: 520px; height: 200px;
    box-sizing: border-box;
    background: var(--yellow);
    border: 8px solid var(--frame);
    border-radius: 30px;
    display: flex;
    align-items: center;
    justify-content: center;
    font-weight: 700;
    font-size: 66px;
    color: var(--ink);
  }
  .mission-text {
    position: absolute;
    left: 108px; top: 1064px;
    margin: 0;
    font-size: 44px;
    font-weight: 700;
    line-height: 92px;
    color: var(--white);
  }
  .supporter-photo {
    position: absolute;
    left: 24px; top: 1960px;
    width: 470px; height: 580px;
    box-sizing: border-box;
    border: 26px solid var(--ink);
    border-radius: 40px;
    background: linear-gradient(140deg, #d7c7b5 0%, var(--photo-cool) 50%, #7a5a44 100%);
    transform: rotate(-9deg);
  }
  .testimonial {
    position: absolute;
    left: 40px; top: 2060px;
    width: 1120px;
    margin: 0;
    font-size: 44px;
    font-weight: 700;
    line-height: 88px;
    text-align: right;
  }
  .testimonial span { display: block; white-space: nowrap; }
  .testimonial .attribution { text-align: left; padding-left: 12px; }
  .brand {
    position: absolute;
    right: 24px; top: 2990px;
    display: flex;
    align-items: center;
    gap: 18px;
    font-weight: 700;
    font-size: 58px;
    color: var(--ink);
  }
  .brand-dot {
    width: 56px; height: 56px;
    border-radius: 50%;
    background: var(--red);
  }
  .bottom-band {
    position: absolute;
    left: 0; top: 3110px;
    width: 760px; height: 36px;
    background: var(--red);
  }
</style>
</head>
<body>
<main class="panel">
  <div class="top-band"></div>

  <div class="hero-photo" role="img" aria-label="Photo of a volunteer sitting on a porch with three smiling children"></div>

  <svg class="mission-shape" viewBox="0 0 1200 3200" aria-hidden="true">
    <polygon points="0,888 1200,790 1200,1880 0,2000" fill="var(--red)"/>
  </svg>

  <div class="section-label">Who we are</div>

  <p class="mission-text">
    a bunch of people who love Jesus<br>
    and love and serve vulnerable kids<br>
    at home and around the world.<br>
    We want to meet the needs<br>
    of the whole child as much as possible,<br>
    by connecting them with<br>
    the people in our community<br>
    and lending our resources and gifts<br>
    to do big things, a little at a time.
  </p>

  <div class="supporter-photo" role="img" aria-label="Photo of a supporter hugging a smiling child"></div>

  <p class="testimonial">
    <span>"For the same amount of</span>
    <span>money I easily spend on</span>
    <span>myself daily, I was helping</span>
    <span>this child have an</span>
    <span>education, shelter, food,</span>
    <span>a chance at life! He was</span>
    <span>so grateful, I was so grateful. I thought</span>
    <span>I would be making a difference in his life,</span>
    <span>but he made a huge difference in mine."</span>
    <span class="attribution">~Terry Vosbeck, Las Vegas, NV</span>
  </p>

  <div class="brand">
    <span class="brand-dot"></span>
    <span>Each Small Lantern</span>
  </div>

  <div class="bottom-band"></div>
</main>
</body>
</html>
```